Flyer Design Project

Training and Consulting Flyer

I attached a document that contained the wording for the flyer as well as the logo.

Target Market(s)

Willow Crest agencies and grantees

Industry/Entity Type

Training

Font styles to use
Sans Serif

Colors
e667a6
eda3c7
a54499
b768aa
f9d9e8

Requirements
Must have
• Words provided on attachment
Nice to have
• Graphics that are related to adult training/learning and consulting

```html
<!DOCTYPE html>
<html lang="en">
<head>
<meta charset="utf-8">
<title>Brightpath Advisors – Flyer</title>
<link rel="stylesheet" href="https://fonts.googleapis.com/css2?family=Oswald:wght@400;600&family=Didact+Gothic&display=swap">
<style>
  :root {
    --magenta: #c2368a;
    --pink: #e667a6;
    --pink-soft: #eda3c7;
    --purple: #a54499;
    --orchid: #b768aa;
    --blush: #f9d9e8;
    --ink: #3a3a3a;
    --paper: #ffffff;
    --mist: #eef0f3;
  }
  * { margin: 0; padding: 0; box-sizing: border-box; }
  html, body { width: 707px; height: 1200px; overflow: hidden; background: var(--mist); }
  .flyer {
    position: relative;
    width: 707px;
    height: 1200px;
    overflow: hidden;
    background: linear-gradient(180deg, var(--paper) 0%, #f6f6f8 100%);
    font-family: "Didact Gothic", "Century Gothic", sans-serif;
    color: var(--ink);
  }
  .hero { position: absolute; top: 0; left: 0; }
  .hero-title, .hero-sub { font-family: "Oswald", sans-serif; }
  .brand-name { font-family: "Didact Gothic", sans-serif; }

  .services {
    position: absolute;
    top: 612px;
    left: 42px;
    width: 625px;
    list-style: none;
  }
  .service {
    position: relative;
    padding-left: 40px;
    margin-bottom: 22px;
    font-size: 14px;
    line-height: 1.5;
  }
  .service-icon {
    position: absolute;
    left: 0;
    top: 2px;
    width: 16px;
    height: 16px;
  }
  .service strong { font-weight: 700; color: var(--ink); }
  .accent { color: var(--magenta); font-weight: 700; }

  .footer { position: absolute; left: 0; bottom: 0; }
</style>
</head>
<body>
<main class="flyer">

  <svg class="hero" width="707" height="600" viewBox="0 0 707 600">
    <defs>
      <linearGradient id="brandBand" x1="0" y1="0" x2="1" y2="1">
        <stop offset="0" stop-color="#b52a80"/>
        <stop offset="1" stop-color="#e667a6"/>
      </linearGradient>
      <radialGradient id="badgeFill" cx="0.4" cy="0.35" r="0.75">
        <stop offset="0" stop-color="#c77bbb"/>
        <stop offset="1" stop-color="#a54499"/>
      </radialGradient>
      <linearGradient id="photoTone" x1="0" y1="0" x2="1" y2="1">
        <stop offset="0" stop-color="#e3d6cf"/>
        <stop offset="0.5" stop-color="#b89a8c"/>
        <stop offset="1" stop-color="#6f7278"/>
      </linearGradient>
      <clipPath id="photoClip">
        <circle cx="560" cy="250" r="340"/>
      </clipPath>
    </defs>

    <circle cx="70" cy="-10" r="260" fill="url(#brandBand)"/>

    <circle cx="560" cy="250" r="356" fill="none" stroke="#e4e4ea" stroke-width="2"/>
    <rect x="0" y="0" width="707" height="600" fill="url(#photoTone)" clip-path="url(#photoClip)"
          role="img" aria-label="Photo of four smiling adult learners gathered around a laptop in a classroom"/>
    <circle cx="560" cy="250" r="340" fill="none" stroke="#ffffff" stroke-width="5"/>

    <text class="brand-name" x="28" y="96" fill="#ffffff" font-size="22">Brightpath Advisors</text>

    <circle cx="225" cy="415" r="142" fill="#ffffff" stroke="#e667a6" stroke-width="2"/>
    <circle cx="225" cy="415" r="130" fill="url(#badgeFill)"/>
    <circle cx="232" cy="276" r="18" fill="#e667a6" stroke="#ffffff" stroke-width="3"/>
    <text class="hero-title" x="225" y="418" text-anchor="middle" fill="#ffffff" font-size="56" font-weight="600" letter-spacing="1">HEALTH</text>
    <text class="hero-sub" x="225" y="454" text-anchor="middle" fill="#ffffff" font-size="23" font-weight="400">CONSULTANTS &amp; GROUP</text>
  </svg>

  <ul class="services">
    <li class="service">
      <svg class="service-icon" viewBox="0 0 16 16"><circle cx="8" cy="4.5" r="3.5" fill="#a54499"/><path d="M1 16 Q1 9 8 9 Q15 9 15 16 Z" fill="#a54499"/></svg>
      Innovative approaches to the meeting the 5 year finding measures in the content area of <strong>Health,Nutrition,Oral Health &amp; Safety.</strong>
    </li>
    <li class="service">
      <svg class="service-icon" viewBox="0 0 16 16"><circle cx="8" cy="4.5" r="3.5" fill="#a54499"/><path d="M1 16 Q1 9 8 9 Q15 9 15 16 Z" fill="#a54499"/></svg>
      <span class="accent">BRIGHTPATH ADVISORS</span> has embarked on a new methodology ensure programes meet total requirments as presentated under health service programmes.
    </li>
    <li class="service">
      <svg class="service-icon" viewBox="0 0 16 16"><circle cx="8" cy="4.5" r="3.5" fill="#a54499"/><path d="M1 16 Q1 9 8 9 Q15 9 15 16 Z" fill="#a54499"/></svg>
      Let us manage your health programme though remote and offsite measures to ensure total compliance and strategic methodology toward quality service approaches.
    </li>
    <li class="service">
      <svg class="service-icon" viewBox="0 0 16 16"><circle cx="8" cy="4.5" r="3.5" fill="#a54499"/><path d="M1 16 Q1 9 8 9 Q15 9 15 16 Z" fill="#a54499"/></svg>
      Let us provide consultants to mentor your health manager nutrition content specialist facilities safety manager. These support consultants are advanced level academias in their specialised areas of focus.
    </li>
    <li class="service">
      <svg class="service-icon" viewBox="0 0 16 16"><circle cx="8" cy="4.5" r="3.5" fill="#a54499"/><path d="M1 16 Q1 9 8 9 Q15 9 15 16 Z" fill="#a54499"/></svg>
      Let us provide evidenced based mock reviews for your programe to assist management staff in focus 1,focus 12,review strategies for <span class="accent">2018.</span>
    </li>
    <li class="service">
      <svg class="service-icon" viewBox="0 0 16 16"><circle cx="8" cy="4.5" r="3.5" fill="#a54499"/><path d="M1 16 Q1 9 8 9 Q15 9 15 16 Z" fill="#a54499"/></svg>
      Let us provide 12 ta for any new health ,nutrition,safety staff to ensure they are fully prepaired to perform their job duties at their higest level of management approaches.
    </li>
  </ul>

  <svg class="footer" width="707" height="150" viewBox="0 0 707 150">
    <defs>
      <linearGradient id="leftBand" x1="0" y1="0" x2="1" y2="0">
        <stop offset="0" stop-color="#b768aa"/>
        <stop offset="1" stop-color="#a54499"/>
      </linearGradient>
      <linearGradient id="rightBand" x1="0" y1="1" x2="1" y2="0">
        <stop offset="0" stop-color="#a54499"/>
        <stop offset="1" stop-color="#c2368a"/>
      </linearGradient>
    </defs>
    <path d="M0 26 Q220 8 460 20" fill="none" stroke="#e667a6" stroke-width="3"/>
    <path d="M0 36 Q220 18 460 30 L460 150 L0 150 Z" fill="url(#leftBand)"/>
    <path d="M707 0 C600 6 470 36 350 150 L707 150 Z" fill="url(#rightBand)"/>
    <path d="M707 0 C600 6 470 36 350 150" fill="none" stroke="#ffffff" stroke-width="3"/>

    <g class="contact-lead" fill="#ffffff">
      <text x="38" y="86" font-size="26">Dana Morrow, CEO</text>
      <line x1="38" y1="98" x2="262" y2="98" stroke="#ffffff" stroke-width="1.5"/>
      <path d="M44 116 q-4 4 0 10 l6 6 q6 4 10 0 l-3 -4 l-4 2 q-4 -2 -6 -6 l2 -4 Z" fill="#ffffff"/>
      <text x="72" y="133" font-size="24">(555)-0142087</text>
    </g>

    <g class="contact-details" fill="#ffffff" font-size="15" text-anchor="end">
      <text x="668" y="42">P.o Box 4821 Fernhill,</text>
      <text x="668" y="62">GA 30999</text>
      <text x="668" y="96">brightpathadvisors@mail.com</text>
      <text x="668" y="126">www.brightpathadvisors.com</text>
    </g>
    <g class="contact-icons" fill="none" stroke="#ffffff" stroke-width="1.5">
      <circle cx="688" cy="37" r="7"/>
      <circle cx="688" cy="91" r="7"/>
      <circle cx="688" cy="121" r="7"/>
      <path d="M688 41 l-2.5 -3.5 a2.5 2.5 0 1 1 5 0 Z" fill="#ffffff" stroke="none"/>
      <rect x="684" y="88" width="8" height="6" fill="#ffffff" stroke="none"/>
      <circle cx="688" cy="121" r="3" fill="#ffffff" stroke="none"/>
    </g>
  </svg>

</main>
</body>
</html>
```